Tombo's Pan. Chicken shop

yDesign special menu with special pictures within 48 h
Very smaple menu

Target Market(s)

Local

Industry/Entity Type

Food

Colors
FFF300
FFF600
FEFA6F
FFFEC7
FFFEE8

Requirements
Must have
• IGood quality picture
Nice to have
• Good quality pictures

```html
<!DOCTYPE html>
<html lang="en">
<head>
<meta charset="utf-8">
<title>Tombo's Pan – Menu Board</title>
<link href="https://fonts.googleapis.com/css2?family=Poppins:wght@400;500;600;700;800;900&family=Oswald:wght@600;700&display=swap" rel="stylesheet">
<style>
  :root{
    --yellow:#ECE51B;
    --yellow-bright:#FFF300;
    --yellow-soft:#F3EC4A;
    --panel:#F0EA3C;
    --ink:#0B0B0B;
    --white:#FFFFFF;
    --red:#E0140F;
    --blue:#1F3FD6;
    --orange:#D98A12;
    --green:#2F9E2A;
    --teal:#1E7FC4;
    --page:#F2F2F2;
  }
  *{box-sizing:border-box;margin:0;padding:0}
  html,body{width:800px;height:1200px;overflow:hidden;background:var(--page)}
  body{font-family:"Poppins",sans-serif;color:var(--ink);position:relative}

  .menu{position:absolute;left:0;top:317px;width:800px;height:565px;background:var(--yellow);overflow:hidden;box-shadow:0 6px 14px rgba(0,0,0,.25)}
  .menu__shapes{position:absolute;inset:0}
  .abs{position:absolute}

  .brand{left:34px;top:42px;width:248px;text-align:center;color:var(--white);font-weight:900;font-size:27px;letter-spacing:.5px;line-height:34px;white-space:nowrap}

  .section-title{font-weight:800;font-size:17px;line-height:17px;color:var(--white);text-transform:uppercase;letter-spacing:.2px}
  .section-sub{font-weight:700;font-size:8px;line-height:10px;color:var(--yellow-bright);margin-top:4px;text-transform:uppercase}
  .section-sub span{text-transform:none}

  .step-col{top:197px;width:118px;height:328px;background:var(--panel);padding:15px 6px 0 6px}
  .step{display:flex;align-items:center;margin:8px 0 5px}
  .step:first-child{margin-top:10px}
  .step__badge{background:var(--ink);color:var(--white);font-family:"Oswald",sans-serif;font-weight:700;font-size:10px;line-height:12px;padding:1px 4px;border-radius:3px;white-space:nowrap}
  .step__note{flex:1;background:var(--white);border-radius:0 4px 4px 0;font-weight:700;font-size:5px;line-height:5.5px;padding:1.5px 4px;margin-left:-1px;text-transform:uppercase}
  .opt{font-size:8.6px;line-height:12.4px;display:flex;justify-content:space-between;align-items:center}

  .price{background:var(--white);color:var(--ink);font-weight:800;font-size:7.4px;line-height:9px;padding:0 4px;border-radius:2px;white-space:nowrap}
  .price--wide{min-width:38px;text-align:right}

  .card{position:absolute;border:1px dashed #CFC41A;border-radius:6px;padding:4px 6px}
  .card--light{border-color:#4a4710}
  .card__head{display:flex;justify-content:space-between;align-items:flex-start;gap:4px}
  .card__name{font-weight:800;font-size:7px;line-height:7px;text-transform:uppercase;color:var(--yellow-bright)}
  .card__desc{font-size:5px;line-height:6px;color:var(--white);margin-top:3px}
  .card--light .card__desc{color:var(--ink)}
  .card__title{font-weight:800;font-size:11px;line-height:12px;color:var(--white);display:flex;align-items:center;gap:3px}
  .card--light .card__title{color:var(--ink)}
  .dot{width:5px;height:5px;border-radius:50%;display:inline-block}
  .card__intro{font-size:8.4px;line-height:10px;color:#d8d8d8;margin:1px 0 4px}
  .card--light .card__intro{color:var(--ink);font-weight:600}
  .cols{display:grid;grid-template-columns:1fr 1fr;column-gap:4px}

  .photo{position:absolute}
  .photo--sandwich{left:714px;top:9px;width:86px;height:170px;border-radius:6px 0 0 6px;background:linear-gradient(170deg,#d9a35c 0%,#6aa03b 35%,#e9b23d 55%,#c98f5a 80%,#a8743e 100%)}
  .photo--meal{left:555px;top:204px;width:245px;height:265px;background:radial-gradient(circle at 70% 70%,#b9652a 0%,#d6472c 35%,#e8c23a 60%,rgba(236,229,27,0) 80%);clip-path:polygon(61% 0,100% 0,100% 100%,0 100%,0 34%,61% 34%)}

  .sides{left:297px;top:350px;width:135px}
  .sides__title{font-weight:800;font-size:11px;color:var(--white);line-height:12px}
  .side{padding:4px 0 8px;border-bottom:1px solid #6b6b6b}
  .side:last-child{border-bottom:none}
  .side__name{font-weight:800;font-size:6.6px;color:var(--yellow-bright);text-transform:uppercase}
  .side__desc{font-size:5px;line-height:6px;color:var(--white)}

  .loaded{left:451px;top:345px;width:90px}
  .loaded__title{font-weight:800;font-size:11px;color:var(--white);line-height:12px;margin-bottom:6px}
  .loaded__item{font-size:5px;line-height:6px;margin-bottom:12px}

  .seasoned{left:559px;top:474px;width:230px}
  .seasoned__title{font-weight:800;font-size:11px;color:var(--white);line-height:13px;margin-bottom:3px}
  .fries{display:grid;grid-template-columns:70px 32px 1fr 32px;column-gap:6px;row-gap:3px;align-items:start}
  .fries__name{font-weight:800;font-size:6.6px;line-height:7px;text-transform:uppercase}
</style>
</head>
<body>
<main class="menu">
  <svg class="menu__shapes" viewBox="0 0 800 565" width="800" height="565" aria-hidden="true">
    <polygon fill="#0B0B0B" points="0,0 800,0 800,200 784,196 770,203 752,198 736,204 720,199 700,205 684,199 666,203 648,197 630,202 612,198 596,204 578,199 560,203 540,197 522,202 504,198 486,203 468,197 450,202 432,196 414,201 396,197 378,202 360,196 342,200 324,195 306,199 288,194 270,198 252,193 234,197 216,192 198,196 180,191 162,195 144,190 126,194 108,190 90,195 72,190 54,194 36,189 18,193 0,190"/>
    <polygon fill="#0B0B0B" points="294,349 304,344 316,350 330,345 344,349 358,343 372,348 388,344 402,349 418,343 434,348 432,380 436,420 431,470 435,520 433,565 299,565 296,520 300,470 295,420 298,380"/>
  </svg>

  <div class="abs brand">TOMBO'S PAN</div>

  <div class="abs" style="left:33px;top:120px">
    <h2 class="section-title">Breaded<br>Wings</h2>
    <p class="section-sub">All wings servied with<br>fries &amp; 1 <span>dip</span></p>
  </div>
  <div class="abs" style="left:162px;top:120px">
    <h2 class="section-title">Buttermilk<br>Marinated<br>Tenders</h2>
    <p class="section-sub">All wings servied with<br>fries &amp; 1 <span>dip</span></p>
  </div>

  <section class="abs step-col" style="left:33px">
    <div class="step"><span class="step__badge">STEP 1</span></div>
    <div class="opt">Wings</div><div class="opt">Boneless</div>
    <div class="step"><span class="step__badge">STEP 2</span></div>
    <div class="opt">4 wings <span class="price price--wide">6.99£</span></div>
    <div class="opt">8 Wings <span class="price price--wide">9.75£</span></div>
    <div class="opt">10 wings <span class="price price--wide">11.50£</span></div>
    <div class="opt">12 Wings <span class="price price--wide">12.95£</span></div>
    <div class="step"><span class="step__badge">STEP 3</span><span class="step__note">Choose<br>your flavour</span></div>
    <div class="opt">1 Original</div><div class="opt">2 buffalo</div><div class="opt">3 bbq</div><div class="opt">4 lemon paper</div><div class="opt">5 garlic parmesan</div><div class="opt">6 dynamite</div><div class="opt">7 Nashville oh hot damn</div>
    <div class="step"><span class="step__badge">STEP 4</span><span class="step__note">Choose<br>your sauce</span></div>
    <div class="opt">Blue cheese</div><div class="opt">Honey mustard</div><div class="opt">House ranch</div><div class="opt">Tombo's special</div>
  </section>

  <section class="abs step-col" style="left:162px">
    <div class="step"><span class="step__badge">STEP 1</span></div>
    <div class="opt">Large</div><div class="opt">Mini</div>
    <div class="step"><span class="step__badge">STEP 2</span></div>
    <div class="opt">3 &nbsp;tenders <span class="price price--wide">6.99£</span></div>
    <div class="opt">6 &nbsp;tenders <span class="price price--wide">9.75£</span></div>
    <div class="step"><span class="step__badge">STEP 3</span><span class="step__note">Choose<br>your flavour</span></div>
    <div class="opt">1 Original</div><div class="opt">2 buffalo</div><div class="opt">3 bbq</div><div class="opt">4 lemon paper</div><div class="opt">5 garlic parmesan</div><div class="opt">6 dynamite</div><div class="opt">7 Nashville oh hot damn</div>
    <div class="step"><span class="step__badge">STEP 4</span><span class="step__note">Choose<br>your sauce</span></div>
    <div class="opt">Blue cheese</div><div class="opt">Honey mustard</div><div class="opt">House ranch</div><div class="opt">Tombo's special</div>
  </section>

  <!-- Sandwich cards on black -->
  <article class="card" style="left:299px;top:50px;width:129px;height:66px">
    <div class="card__title">SANDWICH <span class="dot" style="background:var(--red)"></span></div>
    <p class="card__intro">All meals servied with chips and dip</p>
    <div class="card__head"><span class="card__name">Classic Burger</span><span class="price">5.50£</span></div>
    <p class="card__desc">Fried chicken breast, fresh pickles &amp; creamy mayo in a soft brioche bun</p>
  </article>
  <article class="card" style="left:299px;top:123px;width:129px;height:37px">
    <div class="card__head"><span class="card__name">Tombo's Special</span><span class="price">6.95£</span></div>
    <p class="card__desc">Relish sauce, Fried chicken breast,Honey mustard, Red cabbage in a soft brioche bun</p>
  </article>
  <article class="card" style="left:434px;top:50px;width:128px;height:52px">
    <div class="card__head"><span class="card__name">Nashville oh hot<br>damn</span><span class="price">7.99£</span></div>
    <p class="card__desc">Fried nashville chicken breast, fresh pickles &amp; tombo's sauce, pot of gravy &amp; mash potato</p>
  </article>
  <article class="card" style="left:434px;top:110px;width:128px;height:53px">
    <div class="card__head"><span class="card__name">Double Cheesy<br>Toasted</span><span class="price">5.99£</span></div>
    <p class="card__desc">tenders ,Cheese,<br>slaw, pickles, mayo</p>
  </article>
  <article class="card" style="left:570px;top:50px;width:128px;height:52px">
    <div class="card__head"><span class="card__name">Dynamite Burger</span><span class="price">6.50£</span></div>
    <p class="card__desc">Sweet mayo, Iceberg lettuce, Fried chicken breast, Dynamite sauce , soft deli rolls</p>
  </article>
  <article class="card" style="left:570px;top:110px;width:128px;height:53px">
    <div class="card__head"><span class="card__name">Mini Fillet Slider</span><span class="price">6.50£</span></div>
    <p class="card__desc">lemon herbs , Demled peri<br>peri , mangolime</p>
  </article>

  <div class="photo photo--sandwich" role="img" aria-label="Photo of a stacked club sandwich with lettuce, cheese and ham"></div>
  <div class="photo photo--meal" role="img" aria-label="Photo of a hand dipping fried chicken into sauce beside fries and crispy chicken in a red cup"></div>

  <!-- Build-your-own cards on yellow -->
  <article class="card card--light" style="left:299px;top:210px;width:129px;height:75px">
    <div class="card__title">SANDWICH <span class="dot" style="background:var(--green)"></span></div>
    <p class="card__intro">All meals servied with chips and dip</p>
    <div class="card__head"><span class="card__name" style="color:var(--blue)">Select your base</span><span class="price">2.50£</span></div>
    <p class="card__desc" style="margin-top:1px">Brioche bun<br>soft deli roll<br>Waffle<br>double Chester toasted</p>
  </article>
  <article class="card card--light" style="left:299px;top:290px;width:129px;height:39px">
    <div class="card__head"><span class="card__name" style="color:var(--red)">Select your<br>chicken</span><span class="price">6.95£</span></div>
    <p class="card__desc" style="margin-top:1px">Tenders<br>chicken breast</p>
  </article>
  <article class="card card--light" style="left:434px;top:216px;width:128px;height:69px">
    <div class="card__head"><span class="card__name" style="color:var(--orange)">Select your<br>favourite sause</span><span class="price">7.99£</span></div>
    <div class="card__desc cols"><span>Classic<br>Buffalo<br>Bbq<br>Mango lime</span><span>Daynmat<br>Lemon herbs<br>Nashville<br>Demless peri peri</span></div>
  </article>
  <article class="card card--light" style="left:434px;top:292px;width:128px;height:39px">
    <div class="card__head"><span class="card__name" style="color:var(--green)">Add topping</span><span class="price">7.99£</span></div>
    <div class="card__desc cols"><span>Cheese<br>Lettuce</span><span>Slaw<br>Pickles</span></div>
  </article>
  <article class="card card--light" style="left:570px;top:216px;width:128px;height:69px">
    <div class="card__head"><span class="card__name" style="color:var(--teal)">Select your<br>sause</span><span class="price">6.50£</span></div>
    <p class="card__desc" style="margin-top:1px">Blue cheese<br>Honey mustard<br>House ranch<br>Daynmaite<br>Tombo's special</p>
  </article>

  <section class="abs sides" style="padding:14px 8px 0 8px">
    <h3 class="sides__title">SIDES</h3>
    <div class="side"><div class="card__head"><span class="side__name">Select your base</span><span class="price">5.50£</span></div>
      <p class="side__desc">Chicken pop corn topped with meltd cheddar cheese , dynamite sasue , sismes</p></div>
    <div class="side"><div class="card__head"><span class="side__name">Select your base</span><span class="price">5.50£</span></div>
      <p class="side__desc">Chilli cheese bites ,<br>Select your dip</p></div>
    <div class="side"><div class="card__head"><span class="side__name">Mozerla stick</span><span class="price">5.50£</span></div>
      <p class="side__desc">4 halomi stick<br>5 garlic mushrooms bites<br>6 onion rings<br>Mac &amp; cheese bites<br>Tombo's special<br>Honey mustard slaw</p></div>
  </section>

  <section class="abs loaded">
    <h3 class="loaded__title">LOADED FRIES</h3>
    <p class="loaded__item">Fry by &nbsp;Chips loaded with melted cheese , daynmite sause , jalapeño</p>
    <p class="loaded__item">Takes loaded &nbsp;Chips load3d with melted cheese, &nbsp;hot sause , takes</p>
    <p class="loaded__item">Chickentoos Chips tenders loaded with melted cheese , ketchup, &nbsp;crunchos</p>
    <p class="loaded__item">Oh hot damn<br>Chips nashville tender , melted cheese , sarcha sause , green chilli paper</p>
    <p class="loaded__item">Pop corn &nbsp;Chips Chicken pop corn , melted cheese , Daynmaited sause , Sesame</p>
  </section>

  <section class="abs seasoned">
    <h3 class="seasoned__title">SEASONED FRIES</h3>
    <div class="fries">
      <span class="fries__name">Regular fries</span><span class="price">5.50£</span>
      <span class="fries__name">Cajuan fries</span><span class="price">5.50£</span>
      <span class="fries__name">Regular sweet<br>potato</span><span class="price">5.50£</span>
      <span class="fries__name">Haloomi fries</span><span class="price">5.50£</span>
    </div>
  </section>
</main>
</body>
</html>
```